BuildLinkage.com Full Stationery Design

Business Card will have all info on it. Letterhead will not have name, title or mobile number. Keep general feeling very clean, using colors from the logo as accents.
Name:Dale Vanterpool
Title:President
Phone: 1-800-555-4926
Cell: 306-555-7312
email: dale@buildlinkage.com
website: www.buildlinkage.com
Address:
PO Box 874
Pine Ridge, SK
S0M2T7

Target Market(s)

Construction Business owners

Industry/Entity Type

Business

Contact Information for Business Card

Name:Dale Vanterpool
Title:President
Phone: 1-800-555-4926
Cell: 306-555-7312
Address:
PO Box 874
Pine Ridge, SK
S0M2T7

Font styles to use
Sans Serif

Requirements
Must have
• Clean look
Should not have
• Images or cartoon type characters or tools

```html
<!DOCTYPE html>
<html lang="en">
<head>
<meta charset="utf-8">
<title>BuildLinkage.com Business Card</title>
<link rel="stylesheet" href="https://fonts.googleapis.com/css2?family=Source+Sans+3:wght@400;600&display=swap">
<style>
  :root {
    --backdrop: #5b4b3d;
    --card-white: #ffffff;
    --slate: #48586a;
    --ink: #3e4a58;
    --text-grey: #4a4f57;
    --accent-orange: #e8532a;
    --rule: #55606c;
  }
  * { box-sizing: border-box; margin: 0; padding: 0; }
  html, body {
    width: 1200px; height: 987px; overflow: hidden;
    background: var(--backdrop);
    font-family: "Source Sans 3", sans-serif;
  }
  .stage { position: relative; width: 1200px; height: 987px; }

  .card {
    position: absolute; left: 293px; width: 615px; height: 352px;
  }
  .card--front { top: 130px; background: var(--card-white); }
  .card--back { top: 506px; background: var(--slate); }

  .brand {
    position: absolute; left: 0; right: 0; top: 82px;
    display: flex; justify-content: center; align-items: center; gap: 14px;
  }
  .brand__mark { width: 34px; height: 34px; background: var(--accent-orange); }
  .brand__name {
    font-size: 38px; font-weight: 600; color: var(--ink); letter-spacing: 0.2px;
  }

  .divider {
    position: absolute; left: 42px; right: 43px; top: 211px;
    height: 1px; background: var(--rule);
  }

  .holder { position: absolute; left: 42px; top: 222px; }
  .holder__name { font-size: 23px; font-weight: 600; color: var(--ink); line-height: 30px; }
  .holder__title { font-size: 17px; color: var(--accent-orange); line-height: 22px; }
  .holder__address { margin-top: 4px; font-size: 16px; color: var(--text-grey); line-height: 23px; }

  .contacts {
    position: absolute; right: 42px; top: 225px; list-style: none;
    font-size: 15.5px; color: var(--text-grey);
  }
  .contacts li {
    display: flex; justify-content: flex-end; align-items: center;
    gap: 7px; height: 23.5px;
  }
  .contacts svg { width: 15px; height: 15px; fill: var(--ink); }

  .back-brand {
    position: absolute; left: 0; right: 0; top: 118px;
    display: flex; justify-content: center; align-items: center; gap: 14px;
  }
  .back-brand__mark { width: 40px; height: 40px; background: var(--accent-orange); }
  .back-brand__name { font-size: 40px; font-weight: 600; color: var(--card-white); }
  .back-web {
    position: absolute; left: 0; right: 0; top: 288px;
    text-align: center; font-size: 17px; color: var(--card-white);
  }
</style>
</head>
<body>
<main class="stage">
  <section class="card card--front">
    <div class="brand">
      <span class="brand__mark"></span>
      <span class="brand__name">BuildLinkage.com</span>
    </div>
    <div class="divider"></div>
    <div class="holder">
      <p class="holder__name">Dale Vanterpool</p>
      <p class="holder__title">President</p>
      <p class="holder__address">PO Box 874<br>Pine Ridge, SK, S0M2T7</p>
    </div>
    <ul class="contacts">
      <li>1-800-555-4926
        <svg viewBox="0 0 16 16" aria-hidden="true"><path d="M3.5 1l2.6 2.8-1.4 2a9 9 0 0 0 5.5 5.5l2-1.4L15 12.5 13.2 15C6.5 15 1 9.5 1 2.8z"/></svg>
      </li>
      <li>306-555-7312
        <svg viewBox="0 0 16 16" aria-hidden="true"><path d="M4 0h8a1 1 0 0 1 1 1v14a1 1 0 0 1-1 1H4a1 1 0 0 1-1-1V1a1 1 0 0 1 1-1zm1 2v10h6V2zm3 11a1 1 0 1 0 0 2 1 1 0 0 0 0-2z"/></svg>
      </li>
      <li>dale@buildlinkage.com
        <svg viewBox="0 0 16 16" aria-hidden="true"><path d="M1 3h14v10H1zm1.5 1.2L8 8.5l5.5-4.3z"/></svg>
      </li>
      <li>www.buildlinkage.com
        <svg viewBox="0 0 16 16" aria-hidden="true"><circle cx="8" cy="8" r="7"/><path d="M4 5h3v3H4zM9 9h3v3H9z" fill="#ffffff"/></svg>
      </li>
    </ul>
  </section>

  <section class="card card--back">
    <div class="back-brand">
      <span class="back-brand__mark"></span>
      <span class="back-brand__name">BuildLinkage.com</span>
    </div>
    <p class="back-web">www.buildlinkage.com</p>
  </section>
</main>
</body>
</html>
```